Young Balance Support Network

We need a poster explaining that some children live with a disability called Vestibular Disorder. Feel free to ask question. We want you to respect our color code, same as our logo.

Here is our website : http://www.ybsnetwork.org/

We need to sensibilise people about this disability for children.

Industry/Entity Type

Charity

Font styles to use
Serif

Requirements
Must have
• 1. our logo (with all our details) + one of the photo of Marek
• 2. design showing a child with a dizziness for exemple
• 3. a title saying : Aidez-nous à changer la vie des enfants vivant avec un problème vestibulaire
• 4.include the text attached (information flyer YBSN)
• Poster size : 24"X 36"
Should not have
• wheel chair

```html
<!DOCTYPE html>
<html lang="fr">
<head>
<meta charset="utf-8">
<title>Young Balance Support Network – Poster</title>
<link rel="stylesheet" href="https://fonts.googleapis.com/css2?family=Lato:wght@300;400;700&family=PT+Serif:wght@400&display=swap">
<style>
  :root {
    --sky: #cfe8f4;
    --meadow: #8cc63f;
    --meadow-deep: #5c9e2e;
    --title-box: rgba(86, 186, 232, 0.82);
    --accent: #f7cf1d;
    --ink: #2b2b2b;
    --body: #444444;
    --frame: #e9e9e9;
    --navy: #1d4a7e;
    --brand-green: #8cc63f;
    --brand-blue: #29aee3;
    --white: #ffffff;
  }
  * { margin: 0; padding: 0; box-sizing: border-box; }
  html, body { width: 789px; height: 1200px; overflow: hidden; }
  body { background: var(--frame); position: relative; font-family: 'Lato', sans-serif; color: var(--ink); }

  .top-sheet { position: absolute; left: 0; top: 0; width: 789px; height: 790px; background: var(--white); }
  .content-card { position: absolute; left: 18px; top: 0; width: 753px; height: 1182px; background: var(--white); }

  .hero-photo {
    position: absolute; left: 0; top: 0; width: 789px; height: 548px;
    background:
      radial-gradient(ellipse 230px 260px at 560px 300px, #f2c7a8 0%, #e8b594 55%, rgba(232,181,148,0) 100%),
      linear-gradient(180deg, var(--sky) 0%, #e6f3f8 38%, #b8dc6a 62%, var(--meadow) 78%, var(--meadow-deep) 100%);
  }
  .hero-curve { position: absolute; left: 0; top: 490px; width: 789px; height: 60px; }

  .title-box {
    position: absolute; left: 0; top: 190px; width: 347px; height: 188px;
    background: var(--title-box); color: var(--white); padding: 18px 0 0 55px;
    font-weight: 300; line-height: 1;
  }
  .title-box .t-xl { font-size: 44px; letter-spacing: 0.5px; display: block; }
  .title-box .t-md { font-size: 25px; display: block; margin-top: 8px; }
  .title-box .t-sm { font-size: 16.5px; display: block; margin-top: 8px; }
  .title-box .t-lg { font-size: 44px; display: block; margin-top: 5px; font-weight: 400; }

  .info-block { position: absolute; width: 300px; }
  .info-block .bar { width: 40px; height: 4px; background: var(--accent); margin-bottom: 14px; }
  .info-block h2 { font-weight: 400; font-size: 21px; line-height: 28px; color: var(--ink); letter-spacing: 0.2px; }
  .info-block h2 strong { font-weight: 700; display: block; }
  .info-block p { font-size: 10.4px; line-height: 15.8px; color: var(--body); margin-top: 14px; }
  .info-block p + p { margin-top: 4px; }

  .col-left { left: 54px; }
  .col-right { left: 446px; }
  .row-1 { top: 578px; }
  .row-2 { top: 744px; }
  .info-block.long { width: 310px; }

  .divider { position: absolute; left: 408px; top: 578px; height: 450px; border-left: 1.5px dashed #9a9a9a; }

  .ccp-line { position: absolute; left: 54px; top: 1057px; width: 189px; height: 5px; background: var(--accent); }
  .ccp { position: absolute; left: 260px; top: 1075px; font-size: 22px; color: var(--ink); font-weight: 400; }

  .contact { position: absolute; font-family: 'PT Serif', serif; font-size: 12.5px; color: var(--ink); display: flex; align-items: center; gap: 7px; }
  .contact svg { flex: none; }
  .contact-web { left: 55px; top: 1117px; }
  .contact-mail { left: 55px; top: 1139px; }
  .contact-fb { left: 262px; top: 1117px; }
  .contact-tw { left: 262px; top: 1139px; }
  .social-mark { width: 9px; height: 9px; background: #3b5a96; }
  .social-mark.round { border-radius: 50%; background: #55acee; }

  .brand { position: absolute; left: 525px; top: 1000px; width: 220px; text-align: center; }
  .brand-mark { display: flex; align-items: center; justify-content: center; gap: 8px; }
  .brand-dot { width: 34px; height: 34px; border-radius: 50%; background: var(--brand-blue); }
  .brand-initials { font-family: 'Lato', sans-serif; font-weight: 400; font-size: 22px; letter-spacing: 3px; color: var(--brand-green); }
  .brand-name { font-family: 'PT Serif', serif; font-size: 16px; line-height: 22px; color: var(--navy); margin-top: 38px; letter-spacing: 0.3px; }
</style>
</head>
<body>
  <div class="top-sheet"></div>
  <div class="content-card"></div>

  <div class="hero-photo" role="img" aria-label="Photo of a laughing young child wearing blue glasses in a sunny meadow with yellow flowers and a pale blue sky"></div>
  <svg class="hero-curve" viewBox="0 0 789 60" preserveAspectRatio="none" aria-hidden="true">
    <path d="M0 56 Q394 -2 789 56 L789 60 L0 60 Z" fill="#ffffff"/>
  </svg>

  <h1 class="title-box">
    <span class="t-xl">AIDEZ-NOUS</span>
    <span class="t-md">À CHANGER LA VIE DES</span>
    <span class="t-sm">ENFANTS VIVANT AVEC UN PROBLÈME</span>
    <span class="t-lg">VESTIBULAIRE</span>
  </h1>

  <section class="info-block col-left row-1">
    <div class="bar"></div>
    <h2>QU’EST-CE QUE LE <strong>VESTIBULE ?</strong></h2>
    <p>C’est un organe sensoriel, pilier de votre équilibre, véritable 6ème sens situé dans l’oreille interne.</p>
  </section>

  <section class="info-block col-right row-1">
    <div class="bar"></div>
    <h2>QU’EST CE QU’UNE <strong>ARÉFLEXIE&nbsp; VESTIBULAIRE ?</strong></h2>
    <p>C’est l’absence complète de toute information vestibulaire. L’enfant a ainsi l’impression que tout vacille autour de lui, jour et nuit.</p>
  </section>

  <div class="divider"></div>

  <section class="info-block long col-left row-2">
    <div class="bar"></div>
    <h2>QUELLES EN SONT LES<br>CONSÉQUENCES <strong>POUR L’ENFANT ?</strong></h2>
    <p>Le développement moteur de l’enfant est retardé car il doit trouver des solutions afin de construire son équilibre, stabiliser son regard et son corps.</p>
    <p>Certains apprentissages sont de véritables obstacles pour l’enfant : se représenter son propre corps, se situer dans l’espace qui l’entoure, interagir avec les autres, communiquer, écrire, lire, manger, boire, marcher. Chacune de ces actions necessitent des efforts considérables pour se concentrer quelques secondes ou minutes.</p>
    <p>Quand l’enfant réussit à effectuer l’une de ces actions, son comportement peut sembler déroutant et bien trop souvent mal</p>
  </section>

  <section class="info-block long col-right row-2">
    <div class="bar"></div>
    <h2>QUEL EST LE BUT DE NOTRE <strong>ASSOCIATION ?</strong></h2>
    <p>Notre association a pour but de promouvoir les troubles vestibulaires chez l’enfant, ses conséquences sur sa santé ainsi que celui de son entourage et de soutenir ces enfants et leurs parents en leur offrant un espace de parole et des solutions concrètes pour soulager leur quotidien. Notre association a également pour but de financer et promouvoir toute action de recherche scientifique visant à aider les enfants ayant un trouble vestibulaire.</p>
  </section>

  <div class="ccp-line"></div>
  <div class="ccp">CCP: 12-345678-9</div>

  <div class="contact contact-web">
    <svg width="10" height="10" viewBox="0 0 10 10" aria-hidden="true"><circle cx="5" cy="5" r="4.3" fill="none" stroke="#3a5a8c" stroke-width="1.2"/><path d="M1 5h8M5 0.8c-2 2.6-2 5.8 0 8.4M5 0.8c2 2.6 2 5.8 0 8.4" fill="none" stroke="#3a5a8c" stroke-width="0.9"/></svg>
    <span>www.ybsnetwork.org</span>
  </div>
  <div class="contact contact-mail">
    <svg width="11" height="10" viewBox="0 0 11 10" aria-hidden="true"><path d="M0.5 4.5 L10.5 0.5 L7 9.5 L5 6 Z" fill="#3a5a8c"/></svg>
    <span>info@ybsnetwork.org</span>
  </div>
  <div class="contact contact-fb">
    <span class="social-mark"></span>
    <span>/YoungBalanceSupportNetwork</span>
  </div>
  <div class="contact contact-tw">
    <span class="social-mark round"></span>
    <span>/YBSNAssociation</span>
  </div>

  <div class="brand">
    <div class="brand-mark">
      <span class="brand-dot"></span>
      <span class="brand-initials">YBSN</span>
    </div>
    <div class="brand-name">YOUNG BALANCE SUPPORT<br>NETWORK</div>
  </div>
</body>
</html>
```